Vantrel

I already have a website created through Plovix.com - https://vantrel.co.nz.

Its an accounting services business, can get ideas from tzhl.co.nz, fwu.co.nz, yrx.co.nz

I would like to have this recreated using coding. I need the following features and functionalities incorporated:

- Live Chat feature
- Moving Carousel feature for Reviews
- Advanced SEO support (Google Analytics)

Industry/Entity Type

accounting

Coding

Coded - Design and coding required

Number of Pages Required

5+ page

```html
<!DOCTYPE html>
<html lang="en">
<head>
<meta charset="utf-8">
<title>Vantrel – Our Services</title>
<link href="https://fonts.googleapis.com/css2?family=Montserrat:wght@800&family=Roboto:wght@300;400;500;700&family=Lato:wght@400;700&display=swap" rel="stylesheet">
<style>
:root{
  --ink:#333a3d;
  --muted:#5d6366;
  --teal:#8fbdb2;
  --teal-bright:#8ecabc;
  --teal-deep:#6fa59a;
  --dark:#3e4648;
  --line:#ececec;
  --white:#ffffff;
  --disc-a:#1db3de;
  --disc-b:#0f7e98;
}
*{box-sizing:border-box;margin:0;padding:0}
html,body{width:1200px;height:3089px;overflow:hidden}
body{font-family:'Roboto',sans-serif;color:var(--ink);background:var(--white);position:relative}

.topline{height:10px;background:var(--dark)}
.site-header{position:relative;height:72px;border-bottom:1px solid var(--line)}
.brand{position:absolute;left:62px;top:18px;display:flex;align-items:center;gap:10px;font-family:'Lato',sans-serif;font-weight:700;font-size:22px;color:var(--teal-deep);letter-spacing:1px}
.brand-dot{width:26px;height:26px;border-radius:50%;background:var(--teal)}
.main-nav{position:absolute;left:420px;top:28px;display:flex;gap:21px;font-size:12px;font-weight:400;text-transform:uppercase}
.consult{position:absolute;left:946px;top:0;width:194px;height:72px;background:var(--teal);display:flex;align-items:center;gap:12px;padding-left:16px;color:var(--white)}
.consult small{display:block;font-size:10px;font-family:'Lato',sans-serif}
.consult strong{display:block;font-size:15px;font-family:'Lato',sans-serif;font-weight:400;letter-spacing:.5px}

.hero{position:relative;height:378px;background:linear-gradient(115deg,#4d6a70 0%,#5f7d80 45%,#4b6468 100%)}
.hero h1{position:absolute;left:74px;top:146px;font-family:'Montserrat',sans-serif;font-weight:800;font-size:66px;color:var(--white);letter-spacing:-.5px}

.services{position:relative;height:1562px}
.services-title{position:absolute;top:64px;width:100%;text-align:center;font-size:38px;font-weight:300;color:var(--ink)}
.services-title b{font-weight:700}
.services-intro{position:absolute;top:118px;left:340px;width:520px;text-align:center;font-size:13px;line-height:20px;font-weight:300;color:var(--muted)}
.card{position:absolute;width:277px;height:205px;border:3px solid var(--line);background:var(--white);text-align:center;padding:33px 14px 0}
.card svg{width:40px;height:40px;display:block;margin:0 auto 10px}
.card h3{font-size:13px;font-weight:500;margin-bottom:12px}
.card p{font-size:10px;line-height:15px;font-weight:300;color:var(--ink)}
.guild{position:absolute;left:460px;top:1267px;width:576px;height:205px;border:3px solid var(--line);display:flex;align-items:center;padding-left:62px;gap:50px}
.guild-mark{display:flex;flex-direction:column;align-items:center;gap:10px;width:130px}
.guild-mark span.box{width:54px;height:54px;background:var(--teal)}
.guild-mark span.name{font-size:13px;font-weight:500;color:var(--ink);text-align:center;line-height:16px}
.guild h3{font-size:22px;font-weight:400;margin-bottom:6px}
.guild p{font-size:14px;line-height:22px;font-weight:300;width:330px}

.designed{position:relative;height:358px;background:linear-gradient(100deg,#3c4548 0%,#5b6a6e 50%,#7d8a8c 100%);text-align:center;color:var(--white)}
.designed h2{padding-top:108px;font-size:46px;font-weight:700;color:var(--teal-bright);letter-spacing:.3px}
.designed p{font-size:19px;line-height:29px;font-weight:300;width:900px;margin:4px auto 0}
.btn{display:inline-block;border:2px solid var(--white);color:var(--white);font-size:13px;padding:6px 14px;text-decoration:none}
.designed .btn{margin-top:28px}

.certified{position:relative;height:491px}
.certified h2{position:absolute;left:110px;top:104px;width:560px;font-size:46px;line-height:60px;font-weight:300;color:var(--ink)}
.certified h2 b{font-weight:700;display:block}
.certified p{position:absolute;left:110px;top:264px;width:548px;font-size:13.5px;line-height:19.5px;color:var(--muted)}
.disc{position:absolute;top:146px;width:210px;height:210px;border-radius:50%}
.disc.one{left:698px;background:var(--disc-a)}
.disc.two{left:919px;background:var(--disc-b)}

.cta{position:relative;height:141px;background:var(--teal);color:var(--white)}
.cta p{position:absolute;left:73px;top:36px;font-size:21px;line-height:31px;font-weight:300}
.cta .btn{position:absolute;left:958px;top:54px;font-size:13px;padding:7px 14px}
.chat-bubble{position:absolute;left:1094px;top:82px}

.site-footer{position:relative;height:75px;background:var(--dark);color:var(--white)}
.site-footer small{position:absolute;left:64px;top:30px;font-size:12px}
.social{position:absolute;left:995px;top:22px;display:flex;gap:9px}
.social span{width:28px;height:28px;border-radius:50%;border:1.5px solid var(--white)}
</style>
</head>
<body>
<div class="topline"></div>
<header class="site-header">
  <div class="brand"><span class="brand-dot"></span>VANTREL</div>
  <nav class="main-nav"><span>Home</span><span>Services</span><span>About Us</span><span>Pricing</span><span>Contact Us</span></nav>
  <div class="consult">
    <svg width="44" height="38" viewBox="0 0 44 38" fill="none" stroke="#fff" stroke-width="2"><rect x="2" y="2" width="26" height="18" rx="3"/><path d="M10 20l-4 6 8-6"/><rect x="14" y="12" width="28" height="18" rx="3" fill="#8fbdb2"/><path d="M36 30l4 6-8-6M19 18h18M19 23h14"/></svg>
    <div><small>Get Consultation</small><strong>024837160</strong></div>
  </div>
</header>

<section class="hero" role="img" aria-label="Photo of a calculator, glasses and hands at an accounting desk">
  <h1>OUR SERVICES</h1>
</section>

<section class="services">
  <h2 class="services-title">OUR <b>SERVICES</b></h2>
  <p class="services-intro">We offer a comprehensive suite of accounting services to ensure your organization's financial operations run smoothly and efficiently.</p>

  <div class="card" style="left:145px;top:200px"><svg viewBox="0 0 40 40" fill="none" stroke="#333a3d" stroke-width="1.6"><rect x="5" y="6" width="24" height="26"/><path d="M5 12h24M10 3v6M24 3v6"/><rect x="20" y="20" width="14" height="16" fill="#fff"/><path d="M23 32v-4M27 32v-7M31 32v-5"/></svg><h3>Monthly Reporting</h3><p>Regular, detailed financial reports that give you a clear view of your financial position at all times. From profit and loss statements to cash flow and balance sheets, our reporting is tailored to your needs.</p></div>
  <div class="card" style="left:455px;top:200px"><svg viewBox="0 0 40 40" fill="none" stroke="#333a3d" stroke-width="1.6"><path d="M10 4h16l6 6v26H10z"/><path d="M15 26v-5M19 26v-8M23 26v-4M27 26v-7M14 30h14"/></svg><h3>Annual Financial Statements</h3><p>Preparation of financial statements in line with IFRS/PBE audit-compliant standards for transparency and accountability.</p></div>
  <div class="card" style="left:765px;top:200px"><svg viewBox="0 0 40 40" fill="none" stroke="#333a3d" stroke-width="1.6"><rect x="3" y="14" width="20" height="22"/><path d="M7 20h12M7 25h4M13 25h4M7 30h4M13 30h4"/><circle cx="14" cy="8" r="5"/><circle cx="30" cy="28" r="6"/><path d="M24 12l10-8"/></svg><h3>Cash Flow Reporting</h3><p>Accurate forecasting and monitoring of your cash flow to ensure liquidity and financial stability.</p></div>

  <div class="card" style="left:145px;top:466px"><svg viewBox="0 0 40 40" fill="none" stroke="#333a3d" stroke-width="1.6"><rect x="4" y="5" width="28" height="26"/><path d="M4 11h28M10 27v-6M15 27v-9M20 27v-5M25 27v-10"/><circle cx="32" cy="32" r="6" fill="#fff"/></svg><h3>Budgets &amp; Forecasts</h3><p>Regular, detailed financial reports that give you a clear view of your financial position at all times. From profit and loss statements</p></div>
  <div class="card" style="left:455px;top:466px"><svg viewBox="0 0 40 40" fill="none" stroke="#333a3d" stroke-width="1.6"><path d="M9 4h16l6 6v24H9z"/><path d="M13 14h12M13 19h8"/><rect x="18" y="22" width="16" height="14" fill="#fff"/><path d="M22 27h8M22 31h5"/></svg><h3>GST, PAYE</h3><p>Regular, detailed financial reports that give you a clear view of your financial position at all times. From profit and loss statements</p></div>
  <div class="card" style="left:765px;top:466px"><svg viewBox="0 0 40 40" fill="none" stroke="#333a3d" stroke-width="1.6"><circle cx="11" cy="10" r="7"/><path d="M22 6h12M22 11h8M6 36h30M10 34v-8M17 34v-12M24 34v-6M31 34v-14"/></svg><h3>Financial Performance &amp; Analysis</h3><p>In-depth analysis to track profitability, identify trends, and support strategic decisions.</p></div>

  <div class="card" style="left:145px;top:733px"><svg viewBox="0 0 40 40" fill="none" stroke="#333a3d" stroke-width="1.6"><rect x="10" y="5" width="22" height="28"/><path d="M15 12h12M15 17h12M15 22h8"/><circle cx="11" cy="30" r="6" fill="#fff"/></svg><h3>Payroll</h3><p>Complete payroll management, ensuring timely and compliant processing of employee payments.</p></div>
  <div class="card" style="left:462px;top:733px"><svg viewBox="0 0 40 40" fill="none" stroke="#333a3d" stroke-width="1.6"><circle cx="12" cy="10" r="5"/><path d="M4 26c0-6 4-9 8-9s8 3 8 9"/><path d="M22 20l6-8 4 4 6-10M26 36v-8M31 36v-12M36 36v-16"/><circle cx="12" cy="32" r="4"/></svg><h3>Business Development Advice</h3><p>Expert guidance on financial growth, performance improvement, and sustainable business strategies.</p></div>
  <div class="card" style="left:765px;top:733px"><svg viewBox="0 0 40 40" fill="none" stroke="#333a3d" stroke-width="1.6"><path d="M10 4h16l6 6v24H10z"/><rect x="5" y="18" width="16" height="16" fill="#fff"/><path d="M9 24h8M9 29h8"/><circle cx="29" cy="26" r="5" fill="#fff"/><path d="M33 30l4 4"/></svg><h3>TRA &amp; Audit Compliance</h3><p>Ensuring that your organization meets all TRA tax obligations and audit standards.</p></div>

  <div class="card" style="left:145px;top:1000px"><svg viewBox="0 0 40 40" fill="none" stroke="#333a3d" stroke-width="1.6"><rect x="5" y="5" width="22" height="28"/><circle cx="16" cy="13" r="4"/><path d="M10 22h12M10 27h8"/><rect x="22" y="20" width="14" height="16" fill="#fff"/><path d="M25 25h8M25 29h2M29 29h2M25 32h2M29 32h2"/></svg><h3>Project Accounting</h3><p>Project based accounting support such as reconciliations, rectifying historical transactions, recoding and balance date transition.</p></div>
  <div class="card" style="left:462px;top:1000px"><svg viewBox="0 0 40 40" fill="none" stroke="#333a3d" stroke-width="1.6"><path d="M9 4h16l7 7v25H9z"/><path d="M25 4v7h7"/><rect x="13" y="16" width="15" height="15"/><path d="M13 21h15M13 26h15M18 16v15M23 16v15"/></svg><h3>Sheetwise Templates</h3><p>Tailored, user-friendly Sheetwise templates to streamline financial reporting and analysis.</p></div>
  <div class="card" style="left:765px;top:1000px"><svg viewBox="0 0 40 40" fill="none" stroke="#333a3d" stroke-width="1.6"><path d="M8 14c-4 4-5 10-3 14 2 5 14 5 16 0 2-4 1-10-3-14z"/><path d="M9 14l4-6 4 6"/><path d="M24 36v-8M29 36v-12M34 36v-16M22 20l6-6 4 3 6-8"/></svg><h3>Ledgra Setup &amp; Training</h3><p>Professional setup and hands-on training for Ledgra, LedgraMe, empowering you to manage your finances with confidence and efficiency.</p></div>

  <div class="card" style="left:145px;top:1267px"><svg viewBox="0 0 40 40" fill="none" stroke="#333a3d" stroke-width="1.6"><rect x="5" y="4" width="24" height="30"/><path d="M9 10h10M9 16h4M15 16h10M9 22h4M15 22h10M9 28h4"/><circle cx="30" cy="30" r="5" fill="#fff"/></svg><h3>Audits</h3><p>Tailored audit and financial review services for Tier 3 and Tier 4 charitable trusts with annual expenditure under $550,000.</p></div>

  <div class="guild">
    <div class="guild-mark"><span class="box"></span><span class="name">Registered Accountants Guild</span></div>
    <div><h3>As Chartered Accountants</h3><p>we bring extensive expertise and a personalised approach to help your organisation navigate its financial&nbsp; responsibilities with confidence.</p></div>
  </div>
</section>

<section class="designed" role="img" aria-label="Photo of business people reviewing printed charts with a pen and tablet">
  <h2>THESE SERVICES ARE DESIGNED</h2>
  <p>to support your financial health, compliance, and long-term growth, while delivering high-quality outcomes through expert knowledge and innovative tools.</p>
  <a class="btn" href="#">Contact Us Today</a>
</section>

<section class="certified">
  <h2>We are proud to be<b>Ledgra Advisor Certified</b></h2>
  <p>Providing cloud-based accounting solutions that streamline your financial&nbsp; processes while ensuring accuracy and compliance. Whether you're looking for help with financial reporting, budgeting, grant management, or tax&nbsp; filings, our dedicated team is here to support your growth and success.&nbsp; We're committed to helping you navigate the complexities of accounting,&nbsp; allowing you to focus on what truly matters—achieving your mission and objectives.</p>
  <div class="disc one"></div>
  <div class="disc two"></div>
</section>

<section class="cta">
  <p>I look forward to working alongside you to<br>support your organisation's financial health and future growth.</p>
  <a class="btn" href="#">Contact Us Today</a>
  <svg class="chat-bubble" width="70" height="64" viewBox="0 0 70 64"><path d="M35 4c18 0 32 10 32 24S53 52 35 52c-4 0-8-1-11-2L8 60l5-13C7 42 3 36 3 28 3 14 17 4 35 4z" fill="#a9d0c6"/><circle cx="22" cy="28" r="5" fill="#fff"/><circle cx="35" cy="28" r="5" fill="#fff"/><circle cx="48" cy="28" r="5" fill="#fff"/></svg>
</section>

<footer class="site-footer">
  <small>© 2025 VANTREL.CO.NZ. ALL RIGHTS RESERVED</small>
  <div class="social"><span></span><span></span><span></span></div>
</footer>
</body>
</html>
```